Tri-Fold Brochure Redesign for Floral Preservation Business

I would like to redesign my current tri-fold brouchue that I created myself and have it updated. I would like to keep the same content, color and images, but have it redesigned to look fresher and updated. I'm in the the floral preservation business and work with brides in the wedding inductry. I'm looking for a royal/rustic feel and it should relate to the look and feel of my website www.larkmeadow.com. I have included the Photoshop file I used to create my orginal bouchure.

The only content that has changed is my address which is now;
2847 Birchfall Court, Reston VA 20173

Safe Zone Width - 10.875
Safe Zone Height - 8.375

I have included the Photoshop and Illustrator templates for the tri-fold brochure from the printer I will be using.

```html
<!DOCTYPE html>
<html lang="en">
<head>
<meta charset="utf-8">
<title>Floral Petal Jewelry &amp; Floral Preservation – Brochure Inside</title>
<link rel="stylesheet" href="https://fonts.googleapis.com/css2?family=Pinyon+Script&family=Cormorant+Garamond:wght@500;600&display=swap">
<style>
  :root {
    --plum: #4a0f57;
    --plum-deep: #360a40;
    --plum-soft: #5a1a68;
    --gold: #c9a552;
    --gold-pale: #e6cf8f;
    --cream: #fbf6ec;
    --ink: #4a0f57;
    --stage: #e8e8e8;
    --studio-light: #efefef;
    --studio-mid: #c9c9c9;
    --bust: #2a2a2a;
    --frame-dark: #3a2a22;
    --frame-mid: #7a6252;
    --frame-mat: #e9e1d2;
    --ring-light: #f7e9a8;
    --ring-mid: #e4bf55;
  }
  * { box-sizing: border-box; margin: 0; padding: 0; }
  html, body { width: 1200px; height: 1080px; overflow: hidden; }
  body {
    background: var(--stage);
    font-family: "Cormorant Garamond", Georgia, serif;
    position: relative;
  }
  .brochure {
    position: absolute;
    left: 30px; top: 80px;
    width: 1140px; height: 920px;
    display: flex;
    background: radial-gradient(ellipse at 50% 0%, var(--plum-soft), var(--plum) 55%, var(--plum-deep));
  }
  .panel {
    width: 380px; height: 100%;
    padding: 18px;
    display: flex; flex-direction: column;
    position: relative;
  }
  .panel::before {
    content: "";
    position: absolute; inset: 7px;
    border: 1px solid var(--gold);
    opacity: .65;
    pointer-events: none;
  }
  .panel + .panel { border-left: 1px solid var(--plum-deep); }

  .panel-title {
    height: 52px; margin-bottom: 16px;
    display: flex; align-items: center; justify-content: center; gap: 12px;
    font-family: "Pinyon Script", cursive;
    font-weight: 400;
    font-size: 40px; line-height: 1;
    color: var(--cream);
    white-space: nowrap;
  }
  .panel-title::before, .panel-title::after {
    content: ""; flex: 1; height: 1px;
    background: linear-gradient(90deg, transparent, var(--gold));
  }
  .panel-title::after { background: linear-gradient(90deg, var(--gold), transparent); }

  .card-grid { display: grid; grid-template-columns: 1fr 1fr; column-gap: 16px; }
  .card {
    display: flex; flex-direction: column;
    background: var(--cream);
    border: 1px solid var(--gold);
    padding: 5px 5px 0;
    min-height: 0;
  }
  .card-photo { flex: 1; min-height: 0; border: 1px solid var(--gold-pale); }
  .card-caption {
    height: 40px; flex: none;
    display: flex; align-items: center; justify-content: center;
    text-align: center;
    font-size: 15px; font-weight: 600; line-height: 1.1;
    color: var(--ink);
  }
  .photo-jewelry {
    background: radial-gradient(ellipse 40% 45% at 50% 62%, var(--bust), #555 70%, transparent 100%),
                linear-gradient(180deg, var(--studio-light), var(--studio-mid));
  }
  .photo-rosary { background: linear-gradient(160deg, #ececec, #b9b9b9); }
  .photo-frame {
    background: radial-gradient(ellipse 42% 40% at 50% 50%, var(--frame-mat), var(--frame-mid) 75%, var(--frame-dark));
  }

  .jewelry-grid { grid-template-rows: repeat(3, 260px); row-gap: 18px; }

  .bust-grid { grid-template-rows: repeat(2, 230px); row-gap: 16px; padding: 0 8px; }
  .rosary-grid { grid-template-rows: 130px; margin-top: 18px; }
  .rosary-grid .card-caption, .rosary-single .card-caption { height: 36px; font-size: 14px; }
  .rosary-single { width: 170px; height: 130px; margin: 16px auto 0; flex: none; }

  .contact {
    margin-top: auto;
    text-align: center;
    color: var(--cream);
    padding-bottom: 6px;
  }
  .contact-rule {
    width: 140px; height: 1px; margin: 0 auto 10px;
    background: linear-gradient(90deg, transparent, var(--gold), transparent);
  }
  .contact-web { font-size: 20px; font-weight: 600; color: var(--gold-pale); letter-spacing: .04em; }
  .contact-address { font-size: 16px; font-weight: 500; margin-top: 4px; }

  .frame-grid { grid-template-rows: repeat(3, 180px); row-gap: 12px; column-gap: 14px; }
  .frame-grid .card-caption { height: 52px; font-size: 14px; }

  .rings-photo {
    margin-top: auto;
    height: 170px; flex: none;
    border: 1px solid var(--gold);
    outline: 4px solid var(--cream);
    outline-offset: -6px;
    background: radial-gradient(circle at 78% 22%, var(--ring-light), transparent 50%),
                linear-gradient(135deg, var(--ring-light), var(--ring-mid) 70%, #c29a3d);
  }
</style>
</head>
<body>
<main class="brochure">

  <section class="panel panel-jewelry">
    <h2 class="panel-title">Floral Petal Jewelry</h2>
    <div class="card-grid jewelry-grid">
      <figure class="card"><div class="card-photo photo-jewelry" role="img" aria-label="Necklace, earrings and bracelet set on black display bust"></div><figcaption class="card-caption">Red &amp;<br>White Roses</figcaption></figure>
      <figure class="card"><div class="card-photo photo-jewelry" role="img" aria-label="Lavender and purple jewelry set on black display bust"></div><figcaption class="card-caption">Lavender Rose &amp;<br>Purple Calla Lily</figcaption></figure>
      <figure class="card"><div class="card-photo photo-jewelry" role="img" aria-label="Salmon and blue jewelry set on black display bust"></div><figcaption class="card-caption">Salmon Gerbera &amp;<br>Blue Hydrangea</figcaption></figure>
      <figure class="card"><div class="card-photo photo-jewelry" role="img" aria-label="White jewelry set on black display bust"></div><figcaption class="card-caption">White Roses</figcaption></figure>
      <figure class="card"><div class="card-photo photo-jewelry" role="img" aria-label="Orange and white jewelry set on black display bust"></div><figcaption class="card-caption">Orange Gerbera &amp;<br>White Roses</figcaption></figure>
      <figure class="card"><div class="card-photo photo-jewelry" role="img" aria-label="White and blue jewelry set on black display bust"></div><figcaption class="card-caption">White Rose &amp;<br>Blue Hydrangea</figcaption></figure>
    </div>
  </section>

  <section class="panel panel-middle">
    <div class="card-grid bust-grid">
      <figure class="card"><div class="card-photo photo-jewelry" role="img" aria-label="Yellow jewelry set on black display bust"></div><figcaption class="card-caption">Yellow Calla Lily</figcaption></figure>
      <figure class="card"><div class="card-photo photo-jewelry" role="img" aria-label="Lavender and dark purple jewelry set on black display bust"></div><figcaption class="card-caption">Lavender &amp;<br>Dark Purple Roses</figcaption></figure>
      <figure class="card"><div class="card-photo photo-jewelry" role="img" aria-label="Red jewelry set on black display bust"></div><figcaption class="card-caption">Red Roses</figcaption></figure>
      <figure class="card"><div class="card-photo photo-jewelry" role="img" aria-label="Pink and white jewelry set on black display bust"></div><figcaption class="card-caption">Pink &amp;<br>White Roses</figcaption></figure>
    </div>
    <div class="card-grid rosary-grid">
      <figure class="card"><div class="card-photo photo-rosary" role="img" aria-label="Multicolour petal bead bracelets"></div><figcaption class="card-caption">Assorted Flowers</figcaption></figure>
      <figure class="card"><div class="card-photo photo-rosary" role="img" aria-label="White petal bead rosary with cross"></div><figcaption class="card-caption">White Roses</figcaption></figure>
    </div>
    <figure class="card rosary-single"><div class="card-photo photo-rosary" role="img" aria-label="Blue and white petal bead rosary with cross"></div><figcaption class="card-caption">White Rose &amp; Blue Hydrangea</figcaption></figure>
    <footer class="contact">
      <div class="contact-rule"></div>
      <p class="contact-web">www.larkmeadow.com</p>
      <p class="contact-address">2847 Birchfall Court, Reston VA 20173</p>
    </footer>
  </section>

  <section class="panel panel-preservation">
    <h2 class="panel-title">Floral Preservation</h2>
    <div class="card-grid frame-grid">
      <figure class="card"><div class="card-photo photo-frame" role="img" aria-label="Preserved white bouquet in shadow box frame"></div><figcaption class="card-caption">Bouquet</figcaption></figure>
      <figure class="card"><div class="card-photo photo-frame" role="img" aria-label="Preserved purple bouquet, boutonniere and invitation in frame"></div><figcaption class="card-caption">Bouquet, Boutonniere<br>&amp; Invitation</figcaption></figure>
      <figure class="card"><div class="card-photo photo-frame" role="img" aria-label="Preserved corsage in frame"></div><figcaption class="card-caption">Corsage</figcaption></figure>
      <figure class="card"><div class="card-photo photo-frame" role="img" aria-label="Preserved single white flower in frame"></div><figcaption class="card-caption">Single Flower</figcaption></figure>
      <figure class="card"><div class="card-photo photo-frame" role="img" aria-label="Preserved red bouquet and boutonniere in frame"></div><figcaption class="card-caption">Bouquet &amp; Boutonniere</figcaption></figure>
      <figure class="card"><div class="card-photo photo-frame" role="img" aria-label="Preserved bouquet with invitation, picture and name plate in frame"></div><figcaption class="card-caption">Bouquet, Invitation,<br>Picture and Printed<br>Name Plate</figcaption></figure>
    </div>
    <div class="rings-photo" role="img" aria-label="Gold wedding rings in front of yellow roses"></div>
  </section>

</main>
</body>
</html>
```